Business Card design

We have found an idea we would like to do something similar.
We would require the cards for the inside and the wrapping sheet for the outside, you will see what I mean when you see the image attached. (gum packet) The company is called.... Quillgate Swift Press
I will include the company logo also.
If you could create the outside wrapping with the ability to have staff members name and mobile, maybe on one side panel we would have the address, the other side would be phone numbers, the front would be staff members name and mobile number and email. The other side would be company name and logo if it fits, the logo could wrap around if needed. Open to all ideas.

```html
<!DOCTYPE html>
<html lang="en">
<head>
<meta charset="utf-8">
<title>Quillgate Swift Press – Wrapper Cards</title>
<link rel="stylesheet" href="https://fonts.googleapis.com/css2?family=Oswald:wght@500&family=Arimo:wght@400;700&family=Questrial&display=swap">
<style>
  :root {
    --page: #e6e6e6;
    --card: #ffffff;
    --side: #f1f1f1;
    --edge: #d4d4d4;
    --orange: #f0a11c;
    --ink: #1d1d24;
    --muted: #555a60;
    --navy: #26283a;
    --mark: #ee8a22;
  }
  * { box-sizing: border-box; margin: 0; padding: 0; }
  html, body { width: 1200px; height: 1200px; overflow: hidden; }
  body {
    background: var(--page);
    font-family: "Arimo", Arial, sans-serif;
    color: var(--ink);
    position: relative;
  }
  .wrapper {
    position: absolute;
    left: 210px;
    width: 780px;
    border: 1px solid var(--edge);
    background: var(--card);
  }
  .wrapper--front { top: 120px; }
  .wrapper--back  { top: 680px; }

  .face {
    position: relative;
    height: 260px;
    padding: 36px 44px;
  }
  .side-panel {
    height: 64px;
    background: var(--side);
    border-top: 1px solid var(--edge);
    display: flex;
    align-items: center;
    padding: 0 44px;
    font-size: 24px;
    letter-spacing: 0.5px;
  }

  .staff-name {
    font-family: "Oswald", "Arial Narrow", sans-serif;
    font-weight: 500;
    color: var(--orange);
    font-size: 40px;
    line-height: 1;
    text-transform: uppercase;
    letter-spacing: -0.5px;
  }
  .staff-role {
    color: var(--muted);
    font-size: 24px;
    margin-top: 6px;
  }
  .contact {
    position: absolute;
    right: 44px;
    bottom: 44px;
    text-align: left;
  }
  .contact-phone {
    font-weight: 700;
    font-size: 28px;
  }
  .contact-phone .label { color: var(--orange); margin-right: 6px; }
  .contact-email {
    font-size: 28px;
    margin-top: 4px;
  }

  .brand {
    display: flex;
    align-items: center;
    height: 100%;
    gap: 34px;
    padding-left: 10px;
  }
  .brand-mark { flex: none; }
  .brand-name {
    font-family: "Questrial", "Century Gothic", sans-serif;
    color: var(--navy);
    font-size: 60px;
    line-height: 1.1;
    letter-spacing: 2px;
  }
</style>
</head>
<body>

  <section class="wrapper wrapper--front">
    <div class="face">
      <h1 class="staff-name">Rowan Hale</h1>
      <p class="staff-role">Manager</p>
      <div class="contact">
        <p class="contact-phone"><span class="label">P:</span>555-218-7400</p>
        <p class="contact-email">hello@quillgateswift.com</p>
      </div>
    </div>
    <div class="side-panel">
      <p class="address">Your address, city, state, ZIP 0000</p>
    </div>
  </section>

  <section class="wrapper wrapper--back">
    <div class="face">
      <div class="brand">
        <svg class="brand-mark" width="150" height="150" viewBox="0 0 150 150" aria-hidden="true">
          <circle cx="75" cy="75" r="70" fill="var(--mark)"/>
        </svg>
        <p class="brand-name">Quillgate<br>Swift Press</p>
      </div>
    </div>
    <div class="side-panel"></div>
  </section>

</body>
</html>
```